Need a simple buisness card for my plumbing business. Would like it to be black background with white text.

Industry/Entity Type

Business

Requirements
Must have
• On the front of the card I need to have,
TKB PLUMBING SERVICES
PLUMBERS, DRAINERS & GASFITTERS
Dorian Wellsby
0471596083
Info@tkbplumbingservices.com.au
LIC No 517483f
ABN No 61907354218
On the back I need in point form
Domestic,industrial,commercial, all new installations, renovations, sewer renewals, repairs,
Fully licensed and insured
Nice to have
• A nice simple logo

```html
<!DOCTYPE html>
<html lang="en">
<head>
<meta charset="utf-8">
<title>TKB Plumbing Services – Business Card</title>
<link rel="stylesheet" href="https://fonts.googleapis.com/css2?family=Open+Sans:wght@400;600;700&display=swap">
<style>
  :root {
    --page-bg: #1a1a1a;
    --card-white: #ffffff;
    --card-black: #111214;
    --brand-blue: #1d4f8c;
    --brand-blue-light: #2a86c4;
    --brand-blue-dark: #0f3566;
    --text-dark: #2f2f2f;
    --text-light: #e6e6e6;
    --text-muted: #9a9a9a;
  }
  * { margin: 0; padding: 0; box-sizing: border-box; }
  html, body { width: 1200px; height: 871px; overflow: hidden; }
  body {
    background: var(--page-bg);
    font-family: "Open Sans", sans-serif;
    display: flex;
    flex-direction: column;
    align-items: center;
    justify-content: center;
    gap: 30px;
  }
  .card {
    position: relative;
    width: 700px;
    height: 400px;
    border-radius: 4px;
    overflow: hidden;
  }
  /* Front */
  .card--front { background: var(--card-white); }
  .card__band { position: absolute; left: 0; bottom: 0; width: 700px; height: 400px; }
  .brand-name {
    position: absolute;
    top: 92px;
    left: 0;
    width: 100%;
    text-align: center;
    font-weight: 700;
    font-size: 34px;
    letter-spacing: 0.5px;
    color: var(--brand-blue);
  }
  .contact-person {
    position: absolute;
    top: 178px;
    left: 52px;
  }
  .contact-person__name {
    font-weight: 700;
    font-size: 22px;
    color: var(--brand-blue);
    line-height: 1.1;
  }
  .contact-person__phone {
    display: flex;
    align-items: center;
    gap: 6px;
    font-size: 18px;
    color: var(--text-dark);
    margin-top: 2px;
  }
  .contact-person__phone svg { width: 16px; height: 16px; fill: var(--brand-blue-dark); }
  .company-details {
    position: absolute;
    top: 228px;
    left: 330px;
    font-size: 15.5px;
    line-height: 1.3;
    color: var(--text-dark);
  }
  .company-details__name {
    font-weight: 700;
    font-size: 18px;
    color: var(--brand-blue);
  }
  /* Back */
  .card--back {
    background: linear-gradient(160deg, #222326 0%, var(--card-black) 60%);
    color: var(--text-light);
    text-align: center;
  }
  .card--back .brand-name { color: var(--text-light); top: 80px; }
  .services {
    position: absolute;
    top: 170px;
    left: 0;
    width: 100%;
    list-style: none;
    font-size: 17px;
    line-height: 1.7;
    letter-spacing: 0.5px;
  }
  .services__tagline {
    position: absolute;
    bottom: 48px;
    left: 0;
    width: 100%;
    font-size: 15px;
    font-weight: 600;
    color: var(--text-muted);
    letter-spacing: 1px;
  }
</style>
</head>
<body>
  <section class="card card--front">
    <svg class="card__band" viewBox="0 0 700 400" aria-hidden="true">
      <defs>
        <linearGradient id="bandGradient" x1="0" y1="0" x2="1" y2="0">
          <stop offset="0" stop-color="#0f3566"/>
          <stop offset="0.45" stop-color="#2a86c4"/>
          <stop offset="1" stop-color="#0f3566"/>
        </linearGradient>
      </defs>
      <path d="M0,312 Q260,392 700,392 L700,400 L0,400 Z" fill="url(#bandGradient)"/>
    </svg>

    <div class="brand-name">TKB PLUMBING SERVICES</div>

    <div class="contact-person">
      <div class="contact-person__name">Dorian Wellsby</div>
      <div class="contact-person__phone">
        <svg viewBox="0 0 24 24" aria-hidden="true"><path d="M6.6 10.8a15.1 15.1 0 0 0 6.6 6.6l2.2-2.2a1 1 0 0 1 1-.25 11.4 11.4 0 0 0 3.6.57 1 1 0 0 1 1 1V20a1 1 0 0 1-1 1A17 17 0 0 1 3 4a1 1 0 0 1 1-1h3.5a1 1 0 0 1 1 1c0 1.25.2 2.45.57 3.6a1 1 0 0 1-.25 1z"/></svg>
        <span>0471596083</span>
      </div>
    </div>

    <div class="company-details">
      <div class="company-details__name">TKB PLUMBING SERVICES</div>
      <div>PLUMBERS, DRAINERS &amp; GASFITTERS</div>
      <div>Info@tkbplumbingservices.com.au</div>
      <div>www.tkbplumbingservices.com.au</div>
      <div>LIC No 517483f</div>
      <div>ABN No 61907354218</div>
    </div>
  </section>

  <section class="card card--back">
    <div class="brand-name">TKB PLUMBING SERVICES</div>
    <ul class="services">
      <li>Domestic | Industrial | Commercial</li>
      <li>All new installations | Renovations</li>
      <li>Sewer renewals | Repairs</li>
    </ul>
    <div class="services__tagline">Fully licensed and insured</div>
  </section>
</body>
</html>
```